Design WordPress Website for Contractor App Website

I need a graphic design for a WordPress website for our SaaS called Velturn Software. Please design the landing (Home) page first, before designing other pages. You can design other pages if your landing page is selected.

The design should be modern with a startup feel. The link to the google doc below provides more information. And the attached image has the logo and some screenshots you can use. Copy text from the competitor's site listed as placeholders text or use Lorem Ipsum where needed.

https://files.brindlemark.example/doc/7Qx2Lm9RzT4vKp8NwYc3HsJd5Fg6BtXa/view?mode=read

Target Market(s)

Contractors, painters, plumbers, handymen, electricians, carpenters, landscapers, roofers, home service business.

Industry/Entity Type

Home Improvement

Number of Pages Required

5+ page

Colors
ffc214
34a6d7
9bcb3c

Requirements
Must have
• Look, professionals
Play Store and iOS download download icons
Focused on contractors
Nice to have
• Section for video

```html
<!DOCTYPE html>
<html lang="en">
<head>
<meta charset="utf-8">
<title>Velturn Software – Field Service Management for Contractors</title>
<link href="https://fonts.googleapis.com/css2?family=Montserrat:wght@500;600;700;800&family=Open+Sans:wght@400;600;700&display=swap" rel="stylesheet">
<style>
:root{
  --blue:#2d7ed3;
  --blue-dark:#1f63ad;
  --blue-light:#e8f2fc;
  --orange:#f7941d;
  --ink:#1f2a3a;
  --text:#6b7482;
  --menu:#5a6270;
  --footer:#1b1e25;
  --white:#ffffff;
  --line:#e3e8ef;
}
*{box-sizing:border-box;margin:0;padding:0}
html,body{width:1200px;height:4788px;overflow:hidden}
body{font-family:"Open Sans",Arial,sans-serif;color:var(--text);background:var(--white);position:relative}
h1,h2,h3,h4{font-family:"Montserrat",Arial,sans-serif;color:var(--ink)}
section,header,footer{position:absolute;left:0;width:1200px;overflow:hidden}
.accent{color:var(--orange)}
.blue{color:var(--blue)}
.store-row{display:flex;gap:12px}
.store-badge{display:block;width:124px;height:42px;border-radius:8px;background:#111}
.store-badge.orange{background:var(--orange)}
.phone{position:absolute;background:#f2f3f5;border-radius:34px;border:3px solid #d8dbe0;box-shadow:0 20px 40px rgba(20,40,80,.25)}
.phone .screen{position:absolute;left:10px;right:10px;top:46px;bottom:46px;background:#fff;border-radius:4px;overflow:hidden}
.phone .speaker{position:absolute;top:20px;left:50%;width:56px;height:6px;margin-left:-28px;border-radius:3px;background:#c9ccd2}
.phone .home{position:absolute;bottom:10px;left:50%;width:28px;height:28px;margin-left:-14px;border-radius:50%;border:2px solid #c9ccd2}
.app-bar{height:34px;background:#f26b5b}
.app-row{height:44px;border-bottom:1px solid #eee;display:flex;justify-content:space-between;align-items:center;padding:0 10px;font-size:9px;color:#333}
.app-row b{font-weight:700}
.tag{background:#e6f4d9;color:#4b9b1e;font-size:8px;padding:2px 5px;border-radius:3px}
.tag.red{background:#fde4e1;color:#e04a39}

/* header */
.hero{top:0;height:600px}
.nav{position:absolute;top:16px;left:100px;right:100px;height:48px;display:flex;align-items:center;justify-content:space-between;z-index:2}
.logo{display:flex;align-items:center;gap:10px;font:800 26px "Montserrat",sans-serif;color:var(--blue)}
.logo .mark{width:30px;height:30px;border-radius:50%;background:var(--orange)}
.menu{display:flex;align-items:center;gap:28px;font:600 12px "Montserrat",sans-serif;color:var(--menu)}
.menu .active{color:var(--orange)}
.pill{padding:9px 22px;border-radius:20px;font:700 12px "Montserrat",sans-serif}
.pill.orange{background:var(--orange);color:#fff}
.pill.white{background:#fff;color:var(--blue)}
.hero-copy{position:absolute;left:100px;top:130px;width:520px}
.hero-copy h1{font-size:34px;line-height:1.2;font-weight:800;color:var(--blue);letter-spacing:.3px}
.hero-copy p{margin-top:22px;font-size:13px;line-height:1.7;width:460px}
.hero-copy .store-row{margin-top:24px}
.contacts{margin-top:44px;display:flex;gap:40px;font-size:13px;color:var(--ink)}
.contacts span{display:flex;align-items:center;gap:8px}

/* trusted */
.trusted{top:600px;height:220px;text-align:center}
.trusted h2{margin-top:40px;font-size:28px;font-weight:800;color:var(--orange);letter-spacing:.5px}
.partners{margin:38px auto 0;display:flex;justify-content:center;gap:56px;font:700 16px "Montserrat",sans-serif;color:#8a93a0}
.partners .on{background:var(--blue-light);color:var(--blue);padding:8px 18px;border-radius:4px}

/* video */
.video{top:820px;height:580px}
.video .band{position:absolute;left:0;right:0;top:190px;bottom:0;background:var(--blue)}
.video-frame{position:absolute;left:260px;top:30px;width:680px;height:380px;border:10px solid #fff;box-shadow:0 20px 40px rgba(0,0,0,.2);background:linear-gradient(135deg,#7a5a3a,#b89168 50%,#5c6f86)}
.play{position:absolute;left:50%;top:50%;width:70px;height:70px;margin:-35px 0 0 -35px;border-radius:50%;background:var(--orange);box-shadow:0 0 0 12px rgba(247,148,29,.35)}
.stats{position:absolute;left:300px;right:300px;top:440px;display:flex;justify-content:space-around;text-align:center;color:#fff}
.stats b{display:block;font:800 30px "Montserrat",sans-serif}
.stats span{font:600 11px "Montserrat",sans-serif;letter-spacing:.5px;text-transform:uppercase}
.video .cta{position:absolute;left:540px;top:540px;width:120px;padding:8px 0;text-align:center;background:var(--orange);color:#fff;border-radius:16px;font:700 11px "Montserrat",sans-serif}

/* service */
.service{top:1400px;height:720px}
.service-intro{position:absolute;left:230px;top:100px;width:180px}
.service-intro h2{font-size:38px;line-height:1.1;font-weight:800}
.service-intro p{margin-top:22px;font-size:11px;line-height:1.7}
.view-more{margin-top:180px;font:700 13px "Montserrat",sans-serif;color:var(--blue)}
.card{position:absolute;width:230px;padding:30px 24px;text-align:center;background:#fff;box-shadow:0 12px 36px rgba(30,60,110,.12)}
.card .ic{width:56px;height:56px;margin:0 auto 14px;border-radius:50%;background:var(--blue-light);display:flex;align-items:center;justify-content:center}
.card h3{font-size:18px;font-weight:800;line-height:1.2}
.card p{margin-top:12px;font-size:11px;line-height:1.7}
.card.hot{background:var(--orange)}
.card.hot h3,.card.hot p{color:#fff}
.card.hot .ic{background:rgba(255,255,255,.25)}
.dots{position:absolute;width:120px;height:120px;background-image:radial-gradient(#c6d8ee 2px,transparent 2px);background-size:14px 14px}

/* testimonials */
.reviews{top:2140px;height:440px;background:linear-gradient(180deg,#1a1c21,#23262e);text-align:center}
.reviews h2{margin-top:48px;font-size:30px;font-weight:800;color:#fff}
.review-row{position:absolute;left:210px;top:130px;display:flex;gap:20px}
.review{position:relative;width:246px;height:230px;border:1px solid rgba(255,255,255,.35);padding:22px 20px;text-align:left;color:#c9ced6;font-size:11px;line-height:1.7}
.review .q{font:800 40px Georgia,serif;color:#fff;line-height:.6;height:24px}
.stars{position:absolute;bottom:-8px;left:50%;transform:translateX(-50%);color:var(--orange);font-size:14px;letter-spacing:2px;background:#1f2128;padding:0 6px}
.arrow{position:absolute;top:236px;color:#fff;font-size:26px}

/* app */
.app{top:2580px;height:660px;text-align:center}
.app h2{margin-top:60px;font-size:30px;font-weight:800}
.shot{position:absolute;width:200px;height:300px;top:280px;background:#fff;box-shadow:0 10px 30px rgba(0,0,0,.12);overflow:hidden}
.app .store-row{position:absolute;left:470px;top:595px}

/* get started */
.start{top:3240px;height:600px;background:var(--blue)}
.start .wave{position:absolute;left:0;top:0}
.benefits{position:absolute;left:230px;top:170px;width:380px}
.benefit{display:flex;gap:18px;margin-bottom:40px;color:#fff}
.benefit .bi{flex:0 0 46px;height:46px;border:2px solid rgba(255,255,255,.7);border-radius:8px}
.benefit h4{font:700 17px "Montserrat",sans-serif;color:#fff;text-transform:uppercase}
.benefit p{font-size:11px;line-height:1.6;color:#dbe8f8;margin-top:5px}
.form{position:absolute;left:640px;top:90px;width:330px;height:440px;background:#fff;padding:28px 26px;box-shadow:0 16px 40px rgba(0,0,0,.2)}
.form h3{text-align:center;font-size:20px;font-weight:800;letter-spacing:.5px}
.field{margin-top:18px;height:40px;border:1px solid var(--line);border-radius:3px;padding:11px 12px;font-size:12px;color:#9aa3ad}
.field.msg{height:110px}
.form .submit{margin-top:20px;height:40px;background:var(--orange);color:#fff;text-align:center;font:700 13px/40px "Montserrat",sans-serif;border-radius:3px}

/* blogs */
.blogs{top:3840px;height:460px;text-align:center}
.blogs h2{margin-top:50px;font-size:30px;font-weight:800}
.blog-row{position:absolute;left:205px;top:140px;display:flex;gap:22px}
.post{width:180px;background:#fff;text-align:left;box-shadow:0 8px 24px rgba(0,0,0,.1)}
.post .img{height:140px}
.post h4{padding:14px 12px 6px;font-size:11px;line-height:1.4;font-weight:800}
.post span{display:block;padding:0 12px 16px;font-size:10px;color:var(--orange)}
.blogs .arrow{top:210px;color:#9aa3ad}

/* footer */
.footer{top:4300px;height:488px;background:var(--footer);color:#b4bac4}
.cols{position:absolute;left:210px;top:60px;display:flex;gap:80px}
.col h4{font:800 20px "Montserrat",sans-serif;color:#fff;margin-bottom:14px}
.col li{list-style:none;font-size:11px;line-height:1.9}
.news{position:absolute;left:210px;top:380px}
.news label{display:block;font-size:11px;color:#fff;margin-bottom:8px}
.news .box{display:flex}
.news .in{width:200px;height:34px;background:#fff}
.news .btn{width:92px;height:34px;background:var(--orange);color:#fff;font:700 11px/34px "Montserrat",sans-serif;text-align:center}
.social{position:absolute;left:560px;top:408px;display:flex;gap:8px}
.social i{width:26px;height:26px;border-radius:50%;background:var(--blue)}
.social i:nth-child(2){background:#d9463a}
.copy{position:absolute;left:770px;top:414px;font-size:10px}
</style>
</head>
<body>

<header class="hero">
  <svg width="1200" height="600" style="position:absolute;left:0;top:0" aria-hidden="true">
    <path d="M840 0 H1200 V420 C1100 470 1000 390 920 330 C860 280 830 200 840 120 Z" fill="#2d7ed3"/>
    <path d="M0 520 C220 470 420 560 640 520 C860 480 1000 420 1200 460 V600 H0 Z" fill="#e8f2fc"/>
    <path d="M300 600 C520 540 760 600 960 540 C1060 510 1140 500 1200 510 V600 Z" fill="#2d7ed3"/>
  </svg>
  <nav class="nav">
    <div class="logo"><span class="mark"></span>VELTURN</div>
    <div class="menu">
      <span class="active">HOME</span><span>FEATURES</span><span>PRICING</span><span>SERVICES</span><span>BLOG</span>
      <span class="pill orange">CONTACT</span><span class="pill white">LOGIN</span>
    </div>
  </nav>
  <div class="hero-copy">
    <h1><span class="accent">MOBILE-FIRST</span> FIELD SERVICE MANAGEMENT SOFTWARE &amp; CRM FOR CONTRACTORS</h1>
    <p>Velturn Software is developing the simplest contractor app, a mobile-first field service software &amp; CRM for contractors and home improvement professionals.</p>
    <div class="store-row">
      <span class="store-badge orange" role="img" aria-label="Mobile app download badge"></span>
      <span class="store-badge" role="img" aria-label="Mobile app download badge"></span>
    </div>
    <div class="contacts">
      <span><svg width="14" height="14" viewBox="0 0 24 24"><path d="M6 2l4 4-2 3c1 3 4 6 7 7l3-2 4 4-3 4C10 22 2 14 2 5z" fill="#f7941d"/></svg>(555) 014-2290</span>
      <span><svg width="16" height="12" viewBox="0 0 24 18"><rect x="1" y="1" width="22" height="16" rx="2" fill="none" stroke="#f7941d" stroke-width="2"/><path d="M1 2l11 8 11-8" fill="none" stroke="#f7941d" stroke-width="2"/></svg>hello@velturnsoft.example</span>
    </div>
  </div>
  <div class="phone" style="left:790px;top:70px;width:250px;height:470px">
    <span class="speaker"></span>
    <div class="screen">
      <div class="app-bar"></div>
      <div class="app-row"><b>Leonard Mitton</b><span class="tag">Paid</span></div>
      <div class="app-row"><span>Kitchen remodel</span><b>$420.00</b></div>
      <div class="app-row"><b>Justin Bolton</b><span class="tag red">Due</span></div>
      <div class="app-row"><span>Roof repair</span><b>$1,180.00</b></div>
      <div class="app-row"><b>Mark Steen</b><span class="tag">Paid</span></div>
      <div class="app-row"><span>Deck staining</span><b>$310.00</b></div>
      <div class="app-row"><b>Jimmy Pierson</b><span class="tag red">Due</span></div>
    </div>
    <span class="home"></span>
  </div>
</header>

<section class="trusted">
  <h2>TRUSTED BY MORE THAN <span class="blue">100,000+ CONTRACTORS.</span></h2>
  <div class="partners"><span>Ledgerly</span><span>Toolpost</span><span class="on">Fieldnote</span><span>Paywise</span><span>Datebook</span></div>
</section>

<section class="video">
  <div class="band"></div>
  <div class="video-frame" role="img" aria-label="Video still of a contractor shaking hands with a homeowner"><span class="play"></span></div>
  <div class="stats">
    <div><b>$298+</b><span>Invoices Transactions</span></div>
    <div><b>880+</b><span>Contractors</span></div>
    <div><b>4.5</b><span>Avg. App Rating</span></div>
  </div>
  <div class="cta">GET STARTED →</div>
</section>

<section class="service">
  <span class="dots" style="left:980px;top:40px"></span>
  <span class="dots" style="left:820px;top:520px"></span>
  <div class="service-intro">
    <h2><span class="accent">OUR</span><br><span class="blue">SERVICE</span></h2>
    <p>Send clean estimates, get paid faster and keep every job on track. Built for busy contractors who work from the truck, the site and the office.</p>
    <div class="view-more">VIEW MORE →</div>
  </div>
  <div class="card" style="left:440px;top:150px">
    <div class="ic"><svg width="26" height="26" viewBox="0 0 24 24"><rect x="4" y="2" width="16" height="20" rx="2" fill="none" stroke="#2d7ed3" stroke-width="2"/><path d="M8 8h8M8 12h8M8 16h5" stroke="#2d7ed3" stroke-width="2"/></svg></div>
    <h3>ESTIMATES</h3>
    <p>Create clear, itemized estimates on site and send them to clients in minutes.</p>
  </div>
  <div class="card hot" style="left:690px;top:60px">
    <div class="ic"><svg width="26" height="26" viewBox="0 0 24 24"><rect x="4" y="2" width="16" height="20" rx="2" fill="none" stroke="#fff" stroke-width="2"/><path d="M8 8h8M8 12h8M8 16h5" stroke="#fff" stroke-width="2"/></svg></div>
    <h3>INVOICES</h3>
    <p>Turn approved estimates into invoices with one tap and track what is still due.</p>
  </div>
  <div class="card" style="left:440px;top:410px">
    <div class="ic"><svg width="26" height="26" viewBox="0 0 24 24"><circle cx="12" cy="12" r="9" fill="none" stroke="#2d7ed3" stroke-width="2"/><path d="M12 6v12M15 9h-4a2 2 0 000 4h2a2 2 0 010 4H9" fill="none" stroke="#2d7ed3" stroke-width="2"/></svg></div>
    <h3>PAYMENTS</h3>
    <p>Accept card and bank payments in the field and see deposits land fast.</p>
  </div>
  <div class="card" style="left:690px;top:320px">
    <div class="ic"><svg width="26" height="26" viewBox="0 0 24 24"><path d="M3 11l9-8 9 8v10H3z" fill="none" stroke="#2d7ed3" stroke-width="2"/></svg></div>
    <h3>HOMEOWNER<br>FINANCING</h3>
    <p>Offer simple monthly payment plans so homeowners can say yes to bigger jobs.</p>
  </div>
</section>

<section class="reviews">
  <h2>OUR CUSTOMERS <span class="accent">LOVE US</span></h2>
  <span class="arrow" style="left:150px">←</span>
  <span class="arrow" style="left:1030px">→</span>
  <div class="review-row">
    <div class="review"><div class="q">“</div>Lorem ipsum is simply dummy text of the printing and typesetting industry. It has been the standard dummy text ever since the 1500s, when an unknown printer took a galley of type and scrambled it to make a type specimen book that still reads well.<span class="stars">★★★★★</span></div>
    <div class="review"><div class="q">“</div>Lorem ipsum is simply dummy text of the printing and typesetting industry. It has been the standard dummy text ever since the 1500s, when an unknown printer took a galley of type and scrambled it to make a type specimen book that still reads well.<span class="stars">★★★★★</span></div>
    <div class="review"><div class="q">“</div>Lorem ipsum is simply dummy text of the printing and typesetting industry. It has been the standard dummy text ever since the 1500s, when an unknown printer took a galley of type and scrambled it to make a type specimen book that still reads well.<span class="stars">★★★★★</span></div>
  </div>
</section>

<section class="app">
  <h2><span class="accent">OUR</span> <span class="blue">APP</span></h2>
  <div class="shot" style="left:20px;width:150px" role="img" aria-label="App screen showing the job list"><div class="app-bar"></div><div class="app-row"><b>Leonard</b><span class="tag">Paid</span></div><div class="app-row"><span>Remodel</span><b>$420</b></div><div class="app-row"><b>Justin</b><span class="tag red">Due</span></div></div>
  <div class="shot" style="left:250px" role="img" aria-label="App screen showing invoices"><div class="app-bar" style="background:#2d7ed3"></div><div class="app-row"><b>Gale Anderson</b><span class="tag">Paid</span></div><div class="app-row"><span>Invoice #1042</span><b>$260.00</b></div><div class="app-row"><b>Jeremy Pierson</b><span class="tag red">Due</span></div><div class="app-row"><span>Invoice #1043</span><b>$980.00</b></div><div class="app-row"><b>Mark Steen</b><span class="tag">Paid</span></div></div>
  <div class="shot" style="left:750px" role="img" aria-label="App screen showing a new customer form"><div class="app-bar" style="background:#2d7ed3"></div><div class="app-row"><span>First name</span></div><div class="app-row"><span>Last name</span></div><div class="app-row"><span>Phone</span></div><div class="app-row"><span>Address</span></div><div class="app-row"><span>Notes</span></div></div>
  <div class="shot" style="left:1030px;width:150px" role="img" aria-label="App screen showing the schedule"><div class="app-bar"></div><div class="app-row"><b>Mon 9:00</b></div><div class="app-row"><b>Tue 11:30</b></div><div class="app-row"><b>Wed 14:00</b></div></div>
  <div class="phone" style="left:470px;top:180px;width:260px;height:400px">
    <span class="speaker"></span>
    <div class="screen" role="img" aria-label="App screen showing customer list">
      <div class="app-bar"></div>
      <div class="app-row"><b>Leonard Mitton</b><span class="tag">Paid</span></div>
      <div class="app-row"><b>Justin Bolton</b><span class="tag red">Due</span></div>
      <div class="app-row"><b>Mark Steen</b><span class="tag">Paid</span></div>
      <div class="app-row"><b>Jimmy Pierson</b><span class="tag red">Due</span></div>
      <div class="app-row"><b>Lucia Santos</b><span class="tag">Paid</span></div>
    </div>
    <span class="home"></span>
  </div>
  <div class="store-row">
    <span class="store-badge orange" role="img" aria-label="Mobile app download badge"></span>
    <span class="store-badge" role="img" aria-label="Mobile app download badge"></span>
  </div>
</section>

<section class="start">
  <svg class="wave" width="1200" height="600" aria-hidden="true">
    <path d="M0 0 H1200 V120 C900 40 500 160 0 60 Z" fill="#3a8be0"/>
    <path d="M0 600 V480 C300 560 700 420 1200 520 V600 Z" fill="#1f63ad"/>
  </svg>
  <div class="benefits">
    <div class="benefit"><span class="bi"></span><div><h4>Improve Sales</h4><p>Win more jobs with fast estimates and follow-ups that never slip through the cracks.</p></div></div>
    <div class="benefit"><span class="bi"></span><div><h4>Supercharge Your Team</h4><p>Assign jobs, share notes and keep every crew member on the same page.</p></div></div>
    <div class="benefit"><span class="bi"></span><div><h4>Manage Your Business Easily</h4><p>Clients, invoices and payments in one simple app that works anywhere.</p></div></div>
  </div>
  <div class="form">
    <h3>LET'S GET STARTED</h3>
    <div class="field">Name</div>
    <div class="field">Email</div>
    <div class="field">Phone</div>
    <div class="field msg">Messages</div>
    <div class="submit">GET STARTED</div>
  </div>
</section>

<section class="blogs">
  <h2><span class="blue">LATEST</span> <span class="accent">BLOGS</span></h2>
  <span class="arrow" style="left:165px">‹</span>
  <span class="arrow" style="left:1020px">›</span>
  <div class="blog-row">
    <div class="post"><div class="img" role="img" aria-label="Photo of a contractor team on site" style="background:linear-gradient(135deg,#8fa6bd,#d8c3a2)"></div><h4>LOREM IPSUM HAS BEEN THE INDUSTRY'S STANDARD...</h4><span>MAY 05, 2020</span></div>
    <div class="post"><div class="img" role="img" aria-label="Photo of a worker in a safety vest" style="background:linear-gradient(135deg,#c8b08a,#6f7f92)"></div><h4>LOREM IPSUM HAS BEEN THE INDUSTRY'S STANDARD...</h4><span>MAY 05, 2020</span></div>
    <div class="post"><div class="img" role="img" aria-label="Photo of a worker on a job site" style="background:linear-gradient(135deg,#e0b45a,#8b6a4c)"></div><h4>LOREM IPSUM HAS BEEN THE INDUSTRY'S STANDARD...</h4><span>MAY 05, 2020</span></div>
    <div class="post"><div class="img" role="img" aria-label="Photo of a brick wall project" style="background:linear-gradient(135deg,#b0603e,#d9a07a)"></div><h4>LOREM IPSUM HAS BEEN THE INDUSTRY'S STANDARD...</h4><span>MAY 05, 2020</span></div>
  </div>
</section>

<footer class="footer">
  <div class="cols">
    <div class="col"><h4>FEATURES</h4><ul><li>Dispatching</li><li>Scheduling</li><li>Job Tracking</li><li>Marketing</li><li>Reporting</li><li>Invoicing</li><li>Social Media</li><li>Mobile</li></ul></div>
    <div class="col"><h4>INDUSTRIES</h4><ul><li>HVAC</li><li>Plumbing</li><li>Electrical</li><li>Garage Door</li><li>Landscaping</li><li>Pest Control</li><li>Window Cleaning</li><li>Lawn Care</li></ul></div>
    <div class="col"><h4>RESOURCES</h4><ul><li>Blog</li><li>Webinars</li><li>Podcast</li><li>Company</li><li>Case Studies</li><li>Events</li><li>Guides</li><li>Lawn Care</li></ul></div>
    <div class="col"><h4>COMPANY</h4><ul><li>Company</li><li>Careers</li><li>Partners</li><li>Services</li><li>Pricing</li><li>Blog</li><li>Login</li><li>Contact Us</li></ul></div>
  </div>
  <div class="news"><label>Get our monthly newsletter</label><div class="box"><span class="in"></span><span class="btn">SUBSCRIBE</span></div></div>
  <div class="social"><i></i><i></i><i></i></div>
  <div class="copy">Copyright ©2020 Velturn Software. All rights reserved.</div>
</footer>

</body>
</html>
```